Vintage pharmacy themed coffee bag label

This is a coffee label for the signature blend of a medical apothecary (vintage pharmacy) themed coffee company that donates proceeds to fund medical care around the world.

I want the design to scream old/vintage pharmacy such as examples attached (example-asthmacig, citratemagnesia, french-label, witch-sample ). I'd like the label to roughly mimic the setup of the example-asthmacig but with a bit more intricate lettering and design like the other examples have.

Target Market(s)

Higher end coffee drinkers

Industry/Entity Type

It Company

Font styles to use
Serif
Decorative
Script

Colors
191919
7f7f7f
e0e0e0

Requirements
Must have
• The actual text with basic outline is attached as "Actual text for label." I'd like the photo to be of the doctor attached (Dr Fenwick). I also attached the png of the logo to be included on the label with the website right below it
Nice to have
• Colors should be similar to the attached examples. But mostly black/dark brown font with the off white/brown background
Should not have
• nothing that comes to mind

```html
<!DOCTYPE html>
<html lang="en">
<head>
<meta charset="utf-8">
<title>Kalda Coffee – Dr. Fenwick's Alerta Label</title>
<link rel="stylesheet" href="https://fonts.googleapis.com/css2?family=Abril+Fatface&family=Crimson+Text&family=Montserrat:wght@700&family=Oswald:wght@300;500;700&display=swap">
<style>
  :root {
    --backdrop: #2b2b2b;
    --paper: #efe7d6;
    --paper-edge: #e2d6bd;
    --ink: #1c1a19;
    --red: #9a2229;
    --grey: #7f7f7f;
    --white: #f4efe4;
  }
  * { box-sizing: border-box; margin: 0; padding: 0; }
  html, body {
    width: 1200px; height: 900px; overflow: hidden;
    background: var(--backdrop);
  }
  .canvas { position: relative; width: 1200px; height: 900px; }

  .label {
    position: absolute; left: 360px; top: 50px;
    width: 480px; height: 800px;
    background: radial-gradient(ellipse at center, var(--paper) 55%, var(--paper-edge) 100%);
    border: 6px solid var(--ink);
    color: var(--ink);
  }
  .label__frame { position: absolute; inset: 0; }

  .brand {
    position: absolute; left: 0; right: 0; top: 78px;
    text-align: center;
    font-family: "Oswald", sans-serif; font-weight: 500;
    font-size: 32px; letter-spacing: 3px; color: var(--ink);
  }
  .brand__mark {
    display: inline-block; width: 12px; height: 12px;
    background: var(--ink); margin-right: 10px; vertical-align: middle;
  }

  .portrait {
    position: absolute; left: 74px; top: 205px;
    width: 82px; height: 82px; border-radius: 50%;
    background: radial-gradient(circle at 50% 40%, #c9c4bb 0%, #6b6864 60%, #2a2827 100%);
  }
  .maker {
    position: absolute; left: 198px; top: 214px; width: 250px;
    transform: rotate(-3deg);
    text-align: center;
  }
  .maker__rule { display: block; height: 2px; background: var(--ink); }
  .maker__name {
    display: block; padding: 4px 0 2px;
    font-family: "Oswald", sans-serif; font-weight: 700;
    font-size: 30px; letter-spacing: 2px; line-height: 1.1;
  }

  .product-name {
    position: absolute; left: 24px; width: 420px; top: 300px;
    text-align: center;
    font-family: "Abril Fatface", serif; font-size: 90px; line-height: 1;
    color: var(--red); letter-spacing: 1px;
    text-shadow: 3px 3px 0 var(--ink);
  }

  .claim {
    position: absolute; left: 32px; top: 449px; width: 404px; height: 55px;
    background: var(--ink); color: var(--white);
    border-radius: 4px;
    display: flex; align-items: center; justify-content: center;
    text-align: center;
    font-family: "Montserrat", sans-serif; font-weight: 700;
    font-size: 15.5px; line-height: 1.3; letter-spacing: 0.3px;
  }

  .info { position: absolute; top: 528px; }
  .info__heading {
    font-family: "Oswald", sans-serif; font-weight: 300;
    font-size: 25px; line-height: 1.05; color: var(--red);
    text-transform: uppercase; margin-bottom: 4px;
  }
  .info__body {
    font-family: "Crimson Text", serif; font-size: 14.5px; line-height: 1.3;
  }
  .info--ingredients { left: 48px; width: 130px; }
  .info--directions { left: 204px; width: 236px; }
  .info-divider { position: absolute; left: 184px; top: 530px; }

  .dosage {
    position: absolute; left: 32px; width: 404px; top: 700px;
    border-top: 1.5px solid var(--ink); border-bottom: 1.5px solid var(--ink);
    padding: 4px 0;
    text-align: center;
    font-family: "Oswald", sans-serif; font-weight: 500;
    font-size: 20px; letter-spacing: 1px; color: var(--red);
  }

  .footer {
    position: absolute; left: 40px; right: 40px; top: 744px;
    display: flex; justify-content: space-between;
    font-family: "Oswald", sans-serif; font-weight: 300;
    font-size: 15px; line-height: 20px; letter-spacing: 0.5px;
  }
</style>
</head>
<body>
<div class="canvas">
  <section class="label">
    <svg class="label__frame" width="468" height="788" viewBox="0 0 468 788" aria-hidden="true">
      <rect x="8" y="8" width="452" height="772" fill="none" stroke="#1c1a19" stroke-width="1.5"/>
      <rect x="13" y="13" width="442" height="762" fill="none" stroke="#1c1a19" stroke-width="0.8"/>
    </svg>

    <div class="brand"><span class="brand__mark"></span>KALDA COFFEE</div>

    <div class="portrait" role="img" aria-label="Portrait photograph of Dr. Fenwick"></div>
    <div class="maker">
      <span class="maker__rule"></span>
      <span class="maker__name">DR. FENWICK'S</span>
      <span class="maker__rule"></span>
    </div>

    <h1 class="product-name">ALERTA</h1>

    <div class="claim">FOR THE TEMPORARY RELIEF OF<br>PAROXYSMS OF FATIGUE &amp; EXHAUSTION</div>

    <div class="info info--ingredients">
      <h2 class="info__heading">Active<br>Ingredients</h2>
      <p class="info__body">Iron skillet roasted Ethiopian Yirgacheffe coffee.</p>
    </div>
    <svg class="info-divider" width="10" height="150" viewBox="0 0 10 150" aria-hidden="true">
      <line x1="5" y1="0" x2="5" y2="150" stroke="#1c1a19" stroke-width="1.2"/>
      <circle cx="5" cy="75" r="3" fill="#efe7d6" stroke="#1c1a19" stroke-width="1.2"/>
    </svg>
    <div class="info info--directions">
      <h2 class="info__heading">Directions</h2>
      <p class="info__body">For pour over variety, mix one part coffee to 10 parts water (e.g. 20 g coffee to 200 g water). Coffee grounds to approximate table salt and not to exceed in size the head of a pin.</p>
    </div>

    <p class="dosage">REPEAT EVERY 4 TO 6 HOURS AS NEEDED</p>

    <div class="footer">
      <span>•••• KALDACOFFEE.COM</span>
      <span>NET WT 12 OZ ••••</span>
    </div>
  </section>
</div>
</body>
</html>
```